sydney wedding photography business needs a business card design

we need a business card design for a sydney based wedding photography and videography business. our business name is :golden hour photography and video. our target clients are 24-35 yrs female. our style is candid, organic, natural, dynamic. we are a team of young photographers and videographers, and help brides to create memories that they will cherish for the rest of their lives. the logo will be provided. we want an elegant design that reflects our style, and also want to give a great impression to our clients that we are one of the best studios in sydney and our brand means quality and premium service.

Target Market(s)

bride to be, 24-35 years old, living in sydney and surrunding areas

Industry/Entity Type

Wedding Photography

Contact Information for Business Card

address: 57 marrow lane, bexton nsw 2041
mobile: 0431872056
phone: (02) 9361 2748
info@goldenhourstudio.net.au
www.goldenhourstudio.net.au
facebook:goldenhourbridals
instagram:goldenhourbridals

Font styles to use
Serif
Sans Serif

Requirements
Nice to have
• maybe add my slogan"memories beyond eternity" if the layout looks good
Should not have
• no black color, not good idea for wedding biz card

```html
<!DOCTYPE html>
<html lang="en">
<head>
<meta charset="utf-8">
<title>Golden Hour Photography and Video – Business Card</title>
<link rel="stylesheet" href="https://fonts.googleapis.com/css2?family=Playfair+Display:wght@400;600&family=Lato:wght@400&display=swap">
<style>
  :root {
    --backdrop: #e4e4e2;
    --teal: #0c3f4c;
    --deep-teal: #082a33;
    --gold: #d9a21c;
    --gold-light: #f6d253;
    --gold-deep: #a8741a;
    --bronze: #7a3f2a;
    --paper-white: #ffffff;
  }
  * { margin: 0; padding: 0; box-sizing: border-box; }
  html, body { width: 1200px; height: 1200px; overflow: hidden; }
  body { background: var(--backdrop); position: relative; }

  .card {
    position: absolute;
    width: 778px;
    height: 432px;
    overflow: hidden;
    box-shadow: 0 6px 14px rgba(0,0,0,0.28);
  }

  /* Front */
  .card-front { left: 212px; top: 80px; background: var(--deep-teal); }
  .front-identity {
    position: absolute; left: 0; top: 0; width: 382px; height: 100%;
    background: var(--teal);
    display: flex; flex-direction: column; align-items: center; justify-content: center;
    padding-left: 14px;
  }
  .front-divider {
    position: absolute; left: 382px; top: 0; width: 8px; height: 100%;
    background: linear-gradient(90deg, var(--bronze) 0 22%, var(--gold-light) 40%, var(--gold) 60%, var(--bronze) 78% 100%);
    box-shadow: 3px 0 6px rgba(0,0,0,0.5);
  }
  .holder-name {
    font-family: "Playfair Display", serif;
    font-weight: 600;
    font-size: 44px;
    letter-spacing: 1px;
    background: linear-gradient(180deg, var(--gold-light) 0%, var(--gold) 50%, var(--gold-deep) 100%);
    -webkit-background-clip: text; background-clip: text;
    color: transparent;
    line-height: 1;
  }
  .holder-role {
    font-family: "Playfair Display", serif;
    font-size: 28px;
    color: var(--paper-white);
    margin-top: 12px;
  }

  .contact-list { position: absolute; left: 0; top: 0; width: 100%; height: 100%; list-style: none; }
  .contact-item { position: absolute; left: 450px; display: flex; align-items: center; }
  .contact-icon { width: 28px; height: 28px; flex: none; }
  .contact-text {
    margin-left: 24px;
    font-family: "Playfair Display", serif;
    font-size: 16px;
    line-height: 22px;
    color: var(--paper-white);
    white-space: nowrap;
  }
  .contact-text.sans { font-family: "Lato", sans-serif; font-size: 16px; }
  .item-address { top: 66px; }
  .item-phone { top: 156px; }
  .item-email { top: 253px; }
  .item-web { top: 348px; }

  /* Back */
  .card-back { left: 210px; top: 658px; background: var(--teal); }
  .brand-band {
    position: absolute; left: 0; top: 116px; width: 100%; height: 201px;
    background: var(--deep-teal);
    box-shadow: 0 0 12px rgba(0,0,0,0.5);
    display: flex; align-items: center; justify-content: center;
  }
  .band-rule {
    position: absolute; left: 0; width: 100%; height: 6px;
    background: linear-gradient(90deg, var(--bronze) 0%, var(--gold) 25%, var(--gold-light) 50%, var(--gold) 75%, var(--bronze) 100%);
  }
  .band-rule.top { top: 0; }
  .band-rule.bottom { bottom: 0; }
  .brand-name {
    font-family: "Playfair Display", serif;
    font-weight: 600;
    font-size: 38px;
    color: var(--gold);
    text-align: center;
    white-space: nowrap;
  }
</style>
</head>
<body>

<section class="card card-front" aria-label="Business card front">
  <div class="front-identity">
    <h1 class="holder-name">GOLDEN HOUR</h1>
    <p class="holder-role">Photography &amp; Video</p>
  </div>
  <div class="front-divider"></div>

  <ul class="contact-list">
    <li class="contact-item item-address">
      <svg class="contact-icon" viewBox="0 0 28 28" fill="none" stroke="#d9a21c" stroke-width="1.6">
        <path d="M14 26 C8 18 6 14.5 6 11 a8 8 0 0 1 16 0 c0 3.5 -2 7 -8 15z"/>
        <circle cx="14" cy="11" r="3"/>
      </svg>
      <span class="contact-text">57 Marrow Lane<br>Bexton NSW 2041</span>
    </li>
    <li class="contact-item item-phone">
      <svg class="contact-icon" viewBox="0 0 28 28" fill="none" stroke="#d9a21c" stroke-width="1.6">
        <rect x="8" y="2" width="12" height="24" rx="1.5"/>
        <line x1="8" y1="6" x2="20" y2="6"/>
        <line x1="8" y1="21" x2="20" y2="21"/>
      </svg>
      <span class="contact-text">0431 872 056<br>(02) 9361 2748</span>
    </li>
    <li class="contact-item item-email">
      <svg class="contact-icon" viewBox="0 0 28 28" fill="none" stroke="#d9a21c" stroke-width="1.6">
        <rect x="2" y="7" width="24" height="15"/>
        <path d="M2 7 L14 16 L26 7"/>
        <path d="M2 22 L11 14 M26 22 L17 14"/>
      </svg>
      <span class="contact-text sans">info@goldenhourstudio.net.au</span>
    </li>
    <li class="contact-item item-web">
      <svg class="contact-icon" viewBox="0 0 28 28" fill="none" stroke="#d9a21c" stroke-width="1.6">
        <path d="M3 14 L14 4 L25 14"/>
        <path d="M6 12 V25 H22 V12"/>
        <path d="M12 25 V18 H16 V25"/>
      </svg>
      <span class="contact-text">www.goldenhourstudio.net.au</span>
    </li>
  </ul>
</section>

<section class="card card-back" aria-label="Business card back">
  <div class="brand-band">
    <div class="band-rule top"></div>
    <p class="brand-name">Golden Hour Photography and Video</p>
    <div class="band-rule bottom"></div>
  </div>
</section>

</body>
</html>
```